New Business Card for our Indoor Golf Training Facility

We are looking for designs for a new business card for our indoor golf training facility. Attached is our logo, our logo with our slogan, and here is our elevator pitch (What makes us different from the others) not sure if all the info will fit on one card, maybe you can condense the elevator pitch? here is the info

Elevator Pitch
We work with serious golfers and those that want to be serious golfers…
to make you better, faster, at all phases of the game…
We use the same state-of-the-art technology as professional golfers…
which produces data sets that shows your improvement in real time.
Our facility is available 24/7 to our members, which allows you to improve on your time.

our website: www.brambleteegolf.com

Target Market(s)

Golfers

Font styles to use
Serif
Sans Serif

Colors
ec1f27
f59195
fbd4d5
919191
d3d3d3
1b1b1b

Requirements
Must have
• our logo or our logo with the slogan, elevator pitch (can be condensed or shortened)

```html
<!DOCTYPE html>
<html lang="en">
<head>
<meta charset="utf-8">
<title>Bramble Tee Golf – Business Card</title>
<link href="https://fonts.googleapis.com/css2?family=Lato:wght@400;700;900&display=swap" rel="stylesheet">
<style>
  :root {
    --brand-red: #ec1f27;
    --card-red: #e8413a;
    --pink: #f59195;
    --blush: #fbd4d5;
    --grey: #919191;
    --light-grey: #d3d3d3;
    --ink: #1b1b1b;
    --paper: #ffffff;
  }
  * { margin: 0; padding: 0; box-sizing: border-box; }
  html, body {
    width: 1200px; height: 900px; overflow: hidden;
    background: var(--ink);
    font-family: "Lato", sans-serif;
  }
  .canvas { position: relative; width: 1200px; height: 900px; }

  .card {
    position: absolute;
    width: 560px; height: 320px;
    overflow: hidden;
  }

  /* Back of card */
  .card-back {
    left: 60px; top: 100px;
    background: var(--card-red);
    display: flex; align-items: center; justify-content: center;
  }
  .card-back .faint-ring {
    position: absolute;
    left: 50%; top: 50%;
    width: 190px; height: 190px;
    transform: translate(-50%, -50%);
    border: 18px solid rgba(255,255,255,0.18);
    border-radius: 50%;
  }
  .pitch {
    position: relative;
    list-style: none;
    color: var(--paper);
    font-weight: 700;
    font-size: 12.5px;
    line-height: 1.95;
    text-align: center;
  }

  /* Front of card */
  .card-front {
    left: 580px; top: 480px;
    background: var(--paper);
  }
  .brand {
    position: absolute;
    right: 28px; top: 34px;
    display: flex; align-items: center; gap: 10px;
    color: var(--brand-red);
  }
  .brand-dot {
    width: 34px; height: 34px;
    border: 3px solid var(--brand-red);
    border-radius: 50%;
    flex: none;
  }
  .brand-name {
    font-weight: 900;
    font-size: 30px;
    line-height: 1;
  }
  .brand-slogan {
    font-size: 9.5px;
    margin-top: 3px;
    letter-spacing: 0.2px;
  }
  .contact {
    position: absolute;
    left: 40px; top: 170px;
    color: var(--brand-red);
  }
  .contact-name { font-weight: 700; font-size: 17px; }
  .contact-role { font-size: 12px; margin-bottom: 14px; }
  .contact-line {
    display: flex; align-items: center; gap: 8px;
    font-size: 12px; line-height: 1.55;
  }
  .contact-line svg { width: 11px; height: 11px; fill: var(--brand-red); }
  .contact-web { font-weight: 700; font-size: 12.5px; }
  .swoosh { position: absolute; left: 0; bottom: 0; width: 560px; height: 320px; }
</style>
</head>
<body>
<main class="canvas">

  <section class="card card-back" aria-label="Card back">
    <div class="faint-ring" aria-hidden="true"></div>
    <ul class="pitch">
      <li>We work with serious golfers &amp; those that want to be serious golfers...</li>
      <li>to make you better, faster, at all phases of the game...</li>
      <li>We use the same state-of-the-art technology as professional golfers...</li>
      <li>Which produces data sets that shows your improvement in real time.</li>
      <li>Our facility is available 24/7 to our members, which allows you to improve on your time.</li>
    </ul>
  </section>

  <section class="card card-front" aria-label="Card front">
    <div class="brand">
      <span class="brand-dot" aria-hidden="true"></span>
      <div>
        <div class="brand-name">Bramble Tee Golf</div>
        <div class="brand-slogan">Play Well. Train Smart. Be Better.</div>
      </div>
    </div>

    <div class="contact">
      <div class="contact-name">DANA WHITLOCK</div>
      <div class="contact-role">Managing Director</div>
      <div class="contact-line">
        <svg viewBox="0 0 24 24" aria-hidden="true"><path d="M6.6 10.8a15 15 0 0 0 6.6 6.6l2.2-2.2c.3-.3.7-.4 1-.2 1.1.4 2.3.6 3.6.6.6 0 1 .4 1 1V20c0 .6-.4 1-1 1A17 17 0 0 1 3 4c0-.6.4-1 1-1h3.5c.6 0 1 .4 1 1 0 1.3.2 2.5.6 3.6.1.3 0 .7-.2 1z"/></svg>
        <span>555-014-2277</span>
      </div>
      <div class="contact-line">
        <svg viewBox="0 0 24 24" aria-hidden="true"><path d="M2 5h20v14H2z M2 5l10 8 10-8" /></svg>
        <span>info@brambleteegolf.com</span>
      </div>
      <div class="contact-web">www.brambleteegolf.com</div>
    </div>

    <svg class="swoosh" viewBox="0 0 560 320" aria-hidden="true">
      <path d="M0 320 L0 290 Q330 270 560 105 L560 320 Z" fill="var(--card-red)"/>
      <path d="M250 285 Q430 250 560 95" fill="none" stroke="var(--paper)" stroke-width="5"/>
      <path d="M240 276 Q430 240 560 72 L560 88 Q440 246 240 276 Z" fill="var(--grey)"/>
    </svg>
  </section>

</main>
</body>
</html>
```